K&T Fixit and Rebuild general contracting business card design

I already have a logo that I want to use and I need a card that uses that logo and color scheme on the front with the address phone numbers and email and on the back a place for technicians to write in their name and phone number when they hand it out. It will need the License number of License #KTFXTRB318QN.
It should say General Contractor under the company name. The address is
4417 NE 3rd Ave, Ste D246
Vancouver, WA 98612
www.kandtfixitandrebuild.example
office@kandtfixitandrebuild.example
360-555-0182 is the telephone number
360-555-0149 is the fax number

Target Market(s)

Homeowners needing remodel work or repairs in their home.

Industry/Entity Type

Construction

Contact Information for Business Card

Business name, address, phone number, license number, fax number, email, and website on the front and a place to fill in technician's name and number

Font styles to use
Serif

Requirements
Must have
• Business name, address, phone number, license number, fax number, email, and website on the front and a place to fill in technician's name and number
Nice to have
• I uploaded an example of a front that is good.
Should not have
• Froo froo or extra embellishments.

```html
<!DOCTYPE html>
<html lang="en">
<head>
<meta charset="utf-8">
<title>K&amp;T Fixit and Rebuild — Business Card</title>
<link rel="stylesheet" href="https://fonts.googleapis.com/css2?family=Lora:wght@500;700&display=swap">
<style>
  :root {
    --bg: #ecebe7;
    --paper: #ffffff;
    --ink: #1d1d1d;
    --copper: #b86a3c;
    --copper-faint: #f1e9e3;
    --rule: #6d6d6d;
    --wood-light: #9a6b45;
    --wood-dark: #5f3e24;
    --green: #0f4a37;
    --frame: #f4efe8;
  }
  * { box-sizing: border-box; margin: 0; padding: 0; }
  html, body { width: 1200px; height: 800px; overflow: hidden; }
  body {
    background: var(--bg);
    font-family: "Lora", serif;
    color: var(--ink);
    position: relative;
  }
  .card {
    position: absolute;
    top: 246px;
    width: 540px;
    height: 309px;
    border-radius: 4px;
    overflow: hidden;
    box-shadow: 0 6px 20px rgba(0,0,0,.15);
  }
  .card--front { left: 40px; background: var(--paper); }
  .card--back { left: 620px; }

  /* front */
  .wood-band {
    position: absolute; inset: 0;
    background: linear-gradient(135deg, var(--wood-light), var(--wood-dark));
    clip-path: polygon(300px 309px, 540px 309px, 540px 178px, 330px 178px, 300px 200px);
  }
  .watermark {
    position: absolute; top: 20px; left: 290px;
    font-weight: 700; font-size: 32px; line-height: 1.05;
    color: var(--copper-faint);
  }
  .brand {
    position: absolute; top: 40px; left: 30px;
    display: flex; align-items: center; gap: 10px;
  }
  .brand__mark { width: 22px; height: 22px; background: var(--copper); flex: none; }
  .brand__name { font-weight: 700; font-size: 23px; color: var(--copper); line-height: 1.1; width: 200px; }
  .tagline { position: absolute; top: 112px; left: 62px; font-size: 11px; font-weight: 700; letter-spacing: .12em; color: var(--ink); }
  .rule { position: absolute; height: 1px; background: var(--rule); }
  .rule--top { top: 92px; left: 290px; width: 225px; }
  .rule--bottom { top: 172px; left: 30px; width: 180px; }
  .address { position: absolute; top: 102px; right: 26px; text-align: right; font-size: 12px; font-weight: 500; line-height: 1.55; }
  .license { position: absolute; top: 150px; right: 26px; font-size: 10.5px; font-weight: 700; }
  .license span { color: var(--copper); font-weight: 500; }
  .contacts { position: absolute; top: 184px; left: 30px; list-style: none; font-size: 12px; font-weight: 500; line-height: 1.7; }
  .contacts li { display: flex; align-items: center; gap: 8px; }
  .contacts svg { width: 11px; height: 11px; fill: var(--copper); flex: none; }

  /* back */
  .wood-field {
    position: absolute; inset: 0;
    background: linear-gradient(160deg, var(--wood-light), var(--wood-dark));
  }
  .badge {
    position: absolute; left: 140px; top: 32px; width: 320px; height: 160px;
    background: var(--green);
    border: 3px solid var(--frame);
    border-radius: 6px 30px 6px 30px;
    display: flex; flex-direction: column; align-items: center; justify-content: center; gap: 10px;
  }
  .badge__mark { width: 20px; height: 20px; background: var(--copper); }
  .badge__name { font-weight: 700; font-size: 25px; color: var(--copper); text-align: center; line-height: 1.15; }
  .write-in {
    position: absolute; left: 80px; right: 80px; top: 214px;
    display: flex; flex-direction: column; gap: 16px;
  }
  .write-in__row { display: flex; align-items: flex-end; gap: 10px; }
  .write-in__label { font-size: 12px; font-weight: 700; color: var(--frame); letter-spacing: .06em; width: 92px; flex: none; }
  .write-in__line { flex: 1; height: 1px; background: var(--frame); margin-bottom: 3px; }
</style>
</head>
<body>
  <section class="card card--front" aria-label="Business card front">
    <div class="wood-band" role="img" aria-label="Wood plank texture band"></div>
    <div class="watermark" aria-hidden="true">K&amp;T Fixit<br>and Rebuild</div>
    <div class="brand">
      <span class="brand__mark"></span>
      <span class="brand__name">K&amp;T Fixit and Rebuild</span>
    </div>
    <p class="tagline">GENERAL CONTRACTOR</p>
    <div class="rule rule--top"></div>
    <p class="address">4417 NE 3rd Ave, Ste D246<br>Vancouver, WA 98612</p>
    <p class="license"><span>LIC No :</span> #KTFXTRB318QN</p>
    <div class="rule rule--bottom"></div>
    <ul class="contacts">
      <li><svg viewBox="0 0 24 24"><path d="M6.6 10.8a15 15 0 0 0 6.6 6.6l2.2-2.2a1 1 0 0 1 1-.25 11.4 11.4 0 0 0 3.6.57 1 1 0 0 1 1 1V20a1 1 0 0 1-1 1A17 17 0 0 1 3 4a1 1 0 0 1 1-1h3.5a1 1 0 0 1 1 1c0 1.250.2 2.450.57 3.570a1 1 0 0 1-.25 1z"/></svg>360-555-0182</li>
      <li><svg viewBox="0 0 24 24"><path d="M6 3h10v5H6zM4 9h16a2 2 0 0 1 2 2v7h-4v3H6v-3H2v-7a2 2 0 0 1 2-2zm4 8v2h8v-4H8z"/></svg>360-555-0149</li>
      <li><svg viewBox="0 0 24 24"><path d="M2 5h20v14H2zm2 2v.5l8 5 8-5V7z"/></svg>office@kandtfixitandrebuild.example</li>
      <li><svg viewBox="0 0 24 24"><circle cx="12" cy="12" r="10"/></svg>www.kandtfixitandrebuild.example</li>
    </ul>
  </section>

  <section class="card card--back" aria-label="Business card back">
    <div class="wood-field" role="img" aria-label="Wood plank background"></div>
    <div class="badge">
      <span class="badge__mark"></span>
      <span class="badge__name">K&amp;T Fixit<br>and Rebuild</span>
    </div>
    <div class="write-in">
      <div class="write-in__row"><span class="write-in__label">Technician</span><span class="write-in__line"></span></div>
      <div class="write-in__row"><span class="write-in__label">Phone</span><span class="write-in__line"></span></div>
    </div>
  </section>
</body>
</html>
```